Need Letterhead and Business Card

I have a logo but i need new letterhead and biz cards. We are a real estate investment firm so we need very professional but also do not want to be old fashioned. We have 3 locations; Singapore, New York and Ponte Vedra Florida. I can provide full addresses if needed. If you have adjustments to our logo you would recommend we are open to them.
I will be putting in a separate project but we also need a template for our own powerpoint slide presentations and website.

Real Estate

```html
<!DOCTYPE html>
<html lang="en">
<head>
<meta charset="utf-8">
<title>Keston Stationery</title>
<link rel="stylesheet" href="https://fonts.googleapis.com/css2?family=Montserrat:wght@400;500;600;700&display=swap">
<style>
  :root{
    --navy:#1b5385;
    --gold:#c9a22c;
    --ink:#2b2b2b;
    --paper:#ffffff;
    --backdrop:#ececec;
  }
  *{box-sizing:border-box;margin:0;padding:0}
  html,body{width:1200px;height:900px;overflow:hidden;background:var(--backdrop);font-family:'Montserrat',sans-serif;color:var(--ink)}
  .stage{position:relative;width:1200px;height:900px}

  .letterhead{position:absolute;left:60px;top:54px;width:560px;height:792px;background:var(--paper);box-shadow:0 4px 18px rgba(0,0,0,.12);overflow:hidden}
  .brand{position:absolute;left:48px;top:56px}
  .brand-name{font-weight:700;font-size:34px;letter-spacing:2px;color:var(--navy);line-height:1;display:flex;align-items:center;gap:8px}
  .brand-dot{width:12px;height:12px;border-radius:50%;background:var(--navy);display:inline-block}
  .brand-tag{font-size:6.5px;font-weight:600;letter-spacing:.8px;color:var(--gold);margin-top:5px;text-transform:uppercase}

  .office{position:absolute;right:44px;top:56px;font-size:7px;line-height:1.7;color:var(--navy)}
  .office li{list-style:none;display:flex;align-items:center;gap:5px}
  .office li::before{content:"";width:5px;height:5px;border-radius:50%;background:var(--gold)}
  .office .office-title{font-weight:700}

  .letter-body{position:absolute;left:48px;top:190px;width:464px;font-size:9.4px;line-height:1.5;text-align:justify}
  .letter-body p{margin-bottom:12px}
  .signoff{position:absolute;left:48px;top:470px}
  .signature{width:120px;height:32px;background:linear-gradient(90deg,#e3e9f3,#eef2f8);border-radius:3px}
  .signoff-role{font-size:9.4px;margin-top:4px}

  .letter-footer{position:absolute;left:0;bottom:0;width:560px;height:104px;background:var(--navy);border-top:6px solid var(--gold)}
  .footer-addresses{position:absolute;left:48px;top:34px;display:flex;color:#fff;font-size:8.5px;line-height:1.5}
  .footer-addresses div{padding:0 22px;border-left:1px solid rgba(255,255,255,.6)}
  .footer-addresses div:first-child{border-left:none;padding-left:0}

  .card{position:absolute;width:470px;height:268px;background:var(--paper);box-shadow:0 4px 16px rgba(0,0,0,.13);overflow:hidden}
  .card-panel{position:absolute;top:0;bottom:0;background:var(--navy)}
  .card-contact{top:110px;left:680px}
  .card-contact .card-panel{left:300px;right:0;border-left:6px solid var(--gold)}
  .card-address{top:500px;left:680px}
  .card-address .card-panel{left:0;width:230px;border-right:6px solid var(--gold)}
  .card .brand-name{font-size:30px}
  .card-contact .brand{left:30px;top:60px}
  .card-address .brand{left:258px;top:104px}
  .card-person{position:absolute;left:30px;top:170px;font-size:10px;color:var(--navy)}
  .card-person .person-name{font-weight:600;font-size:12px}
  .card-person .person-mail{margin-top:14px;font-size:8.5px;display:flex;align-items:center;gap:5px}
  .card-person .person-mail::before{content:"";width:5px;height:5px;border-radius:50%;background:var(--gold)}
  .card-office{position:absolute;left:326px;top:104px;font-size:8px;line-height:1.8;color:#fff}
  .card-office li{list-style:none;display:flex;align-items:center;gap:5px}
  .card-office li::before{content:"";width:5px;height:5px;border-radius:50%;background:var(--gold)}
  .card-office .office-title{font-weight:700}
  .card-locations{position:absolute;left:30px;top:60px;color:#fff;font-size:9px;line-height:1.45}
  .card-locations p{margin-bottom:10px}
</style>
</head>
<body>
<main class="stage">

  <section class="letterhead">
    <header class="brand">
      <div class="brand-name"><span class="brand-dot"></span>KESTON</div>
      <div class="brand-tag">Real Estate Investment &amp; Management</div>
    </header>
    <ul class="office">
      <li class="office-title">NEW YORK OFFICE</li>
      <li>212 480 7715</li>
      <li>212 480 7716</li>
      <li>www.kestonrealty.com</li>
    </ul>

    <article class="letter-body">
      <p>Letterhead samples are a great way of deciding what kind of letterhead you want to design for you and your company. The internet has a ton of great letterhead samples to browse through. Whether you want something simple, with just a couple lines of text or your business information, or something decorative and stunning, with photos and logos on the top and bottom of the page, it will be easy to find what you want, because there are samples online for basically any type of letterhead you could want.</p>
      <p>Any business could easily benefit from browsing through some letterhead samples, if only to get an idea for what kind of letterhead their company might want. Letterheads are just one of the tools that a business professional could use to help increase their customer base, and to really be memorable to everyone they write a letter to. Letterhead is quite an effective tool for marketing and advertising, but because it's such a simple and well known idea, it is often unfairly overlooked. Make sure you don't make that mistake, and make some letterhead samples of your own today.</p>
      <p>Whether you want to get new customers to remember you and become part of your clientele, or you just want to send out friendly reminders to your existing clients, customizing your own letterhead samples can really help you out. Try out some letterhead samples and you will not regret it, and I'm sure you will add a new tool to your business' arsenal of networking, marketing, and advertising tools.</p>
    </article>

    <div class="signoff">
      <div class="signature" role="img" aria-label="Handwritten signature of Daniel Marlowe"></div>
      <div class="signoff-role">company director</div>
    </div>

    <footer class="letter-footer">
      <div class="footer-addresses">
        <div>18 Marina Quay<br>Singapore</div>
        <div>240 Hudson Row<br>New York</div>
        <div>71 Dune Court<br>Ponte Vedra</div>
      </div>
    </footer>
  </section>

  <section class="card card-contact">
    <div class="card-panel"></div>
    <header class="brand">
      <div class="brand-name"><span class="brand-dot"></span>KESTON</div>
      <div class="brand-tag">Real Estate Investment &amp; Management</div>
    </header>
    <div class="card-person">
      <div class="person-name">Daniel Marlowe</div>
      <div>managing director</div>
      <div class="person-mail">daniel@kestonrealty.com</div>
    </div>
    <ul class="card-office">
      <li class="office-title">NEW YORK OFFICE</li>
      <li>212 480 7715</li>
      <li>212 480 7716</li>
      <li>www.kestonrealty.com</li>
    </ul>
  </section>

  <section class="card card-address">
    <div class="card-panel"></div>
    <div class="card-locations">
      <p>18 Marina Quay<br>Singapore</p>
      <p>240 Hudson Row<br>New York</p>
      <p>71 Dune Court<br>Ponte Vedra</p>
    </div>
    <header class="brand">
      <div class="brand-name"><span class="brand-dot"></span>KESTON</div>
      <div class="brand-tag">Real Estate Investment &amp; Management</div>
    </header>
  </section>

</main>
</body>
</html>
```